Stationery Required - Own Logo provided

Hi,

We are a retail company called 'Copperfinch Trading Limited' based in the UK and would like some corporate stationery designed.

We have provided our Logo which we would like to use (Its attached to this brief)...

The designs must be orginal, professional, stylish and interesting!

Target Market(s)

We will use this stationery to communicate with our wholesale suppliers and employees, so it must have a 'professional' feel about it.

Industry/Entity Type

It Company

Requirements
Must have
• Must be professional, corporate, stylish and not to 'fussy'. we require ... Business card design, a4 letter, compliment slip. All designs must be supplied in a format where the text (address/telephone numbers etc..) can be edited, as we have alot of staff and operate out of several different premises.
Nice to have
• I would like a windows backround picture file supplied as well so we can integrate that onto our computer systems.

```html
<!DOCTYPE html>
<html lang="en">
<head>
<meta charset="utf-8">
<title>Copperfinch Trading Limited — Stationery</title>
<link href="https://fonts.googleapis.com/css2?family=Open+Sans:wght@400;600&display=swap" rel="stylesheet">
<style>
  :root{
    --forest:#3a5527;
    --lime:#8dc63f;
    --paper:#ffffff;
    --ink:#2f2f2f;
    --backdrop:#e7e4e1;
  }
  *{margin:0;padding:0;box-sizing:border-box}
  html,body{width:1200px;height:900px;overflow:hidden}
  body{background:var(--backdrop);font-family:"Open Sans",Arial,sans-serif;color:var(--ink);position:relative}
  .sheet{position:absolute;background:var(--paper);box-shadow:0 1px 4px rgba(0,0,0,.18);overflow:hidden}
  .brand{display:flex;align-items:center;gap:7px;color:var(--forest);font-weight:600;line-height:1.05}
  .brand-mark{background:var(--lime);flex:none}
  .contact{display:flex;font-size:10.5px;line-height:1.35}
  .contact-block{border-left:1px solid var(--ink);padding-left:6px;margin-right:8px}
  .contact-row{display:flex;align-items:center;gap:3px}
  .icon{width:10px;height:8px;flex:none}
  .footer-band{position:absolute;left:0;background:var(--forest);color:#fff;font-size:11.5px;letter-spacing:2.2px;display:flex;align-items:center;justify-content:flex-end}
  .footer-square{position:absolute;background:var(--lime)}

  .letterhead{left:38px;top:67px;width:548px;height:776px}
  .letterhead .brand{position:absolute;left:30px;top:24px;font-size:16px}
  .letterhead .brand-mark{width:16px;height:16px}
  .letterhead .contact{position:absolute;left:252px;top:29px}
  .letterhead .footer-band{top:741px;width:486px;height:21px;padding-right:14px}
  .letterhead .footer-square{left:492px;top:734px;width:34px;height:34px}

  .card-front{left:657px;top:98px;width:232px;height:132px}
  .card-front .brand{position:absolute;left:16px;top:11px;font-size:11px}
  .card-front .brand-mark{width:11px;height:11px}
  .card-name{position:absolute;left:16px;top:47px;color:var(--forest);font-weight:600;font-size:11px;line-height:1.1}
  .card-role{display:block;color:var(--ink);font-weight:400;font-size:6.5px}
  .card-details{position:absolute;left:16px;top:75px;font-size:6.5px;line-height:1.45}
  .card-front .footer-band{top:114px;width:196px;height:12px}
  .card-front .footer-square{left:201px;top:104px;width:22px;height:22px}

  .card-back{left:907px;top:98px;width:232px;height:132px;background:var(--forest)}
  .card-back .brand{position:absolute;left:0;right:0;top:34px;flex-direction:column;gap:6px;color:#fff;font-size:13px;text-align:center}
  .card-back .brand-mark{width:26px;height:26px}
  .card-back .lime-band{position:absolute;left:0;top:114px;width:232px;height:12px;background:var(--lime);color:#fff;font-size:6.5px;letter-spacing:1.2px;text-align:center;line-height:12px}

  .compliment{left:621px;top:267px;width:549px;height:259px}
  .compliment .brand{position:absolute;left:23px;top:17px;font-size:16px}
  .compliment .brand-mark{width:16px;height:16px}
  .compliment .contact{position:absolute;left:229px;top:20px}
  .compliment .footer-band{top:224px;width:482px;height:21px;padding-right:12px}
  .compliment .footer-square{left:488px;top:209px;width:36px;height:36px}

  .cover{left:621px;top:553px;width:549px;height:259px;background:var(--forest)}
  .cover .brand{position:absolute;left:0;right:0;top:66px;flex-direction:column;gap:12px;color:#fff;font-size:22px;text-align:center}
  .cover .brand-mark{width:62px;height:62px}
  .cover .lime-band{position:absolute;left:0;top:222px;width:549px;height:24px;background:var(--lime);color:#fff;font-size:11.5px;letter-spacing:2.2px;text-align:center;line-height:24px}
</style>
</head>
<body>

<svg width="0" height="0" style="position:absolute">
  <defs>
    <symbol id="phone" viewBox="0 0 10 8"><path d="M1 3c0-2 8-2 8 0v1H7V3H3v1H1z M3 4h4l1 3H2z" fill="#8dc63f"/></symbol>
    <symbol id="mail" viewBox="0 0 10 8"><rect x=".5" y=".5" width="9" height="7" fill="none" stroke="#8dc63f"/><path d="M.5 .5 5 4.5 9.5 .5" fill="none" stroke="#8dc63f"/></symbol>
  </defs>
</svg>

<section class="sheet letterhead">
  <div class="brand"><span class="brand-mark"></span><span>Copperfinch<br>Trading Limited</span></div>
  <div class="contact">
    <div class="contact-block">17 harbour lane, Millbrook<br>County Down BT30 4QX</div>
    <div class="contact-block">
      <div class="contact-row"><svg class="icon"><use href="#phone"/></svg>: 0700-555-0142</div>
      <div class="contact-row"><svg class="icon"><use href="#mail"/></svg>: copperfinch@mailbox.co.uk</div>
    </div>
  </div>
  <div class="footer-band">www.copperfinch.co.uk</div>
  <div class="footer-square"></div>
</section>

<section class="sheet card-front">
  <div class="brand"><span class="brand-mark"></span><span>Copperfinch<br>Trading Limited</span></div>
  <div class="card-name">Martin Doyle<span class="card-role">Company Director</span></div>
  <div class="card-details">
    17 harbour lane, Millbrook<br>County Down BT30 4QX
    <div class="contact-row"><svg class="icon" style="width:7px;height:6px"><use href="#phone"/></svg>: 0700-555-0142</div>
    <div class="contact-row"><svg class="icon" style="width:7px;height:6px"><use href="#mail"/></svg>: copperfinch@mailbox.co.uk</div>
  </div>
  <div class="footer-band"></div>
  <div class="footer-square"></div>
</section>

<section class="sheet card-back">
  <div class="brand"><span class="brand-mark"></span><span>Copperfinch Trading Limited</span></div>
  <div class="lime-band">www.copperfinch.co.uk</div>
</section>

<section class="sheet compliment">
  <div class="brand"><span class="brand-mark"></span><span>Copperfinch<br>Trading Limited</span></div>
  <div class="contact">
    <div class="contact-block">17 harbour lane, Millbrook<br>County Down BT30 4QX</div>
    <div class="contact-block">
      <div class="contact-row"><svg class="icon"><use href="#phone"/></svg>: 0700-555-0142</div>
      <div class="contact-row"><svg class="icon"><use href="#mail"/></svg>: copperfinch@mailbox.co.uk</div>
    </div>
  </div>
  <div class="footer-band">www.copperfinch.co.uk</div>
  <div class="footer-square"></div>
</section>

<section class="sheet cover">
  <div class="brand"><span class="brand-mark"></span><span>Copperfinch Trading Limited</span></div>
  <div class="lime-band">www.copperfinch.co.uk</div>
</section>

</body>
</html>
```